Photographic Tutorial website

We are looking for a fresh design for a photographic tutorial / workshop website. The website will have the included functions:

* Home (needs to have a login section)
* About Us
* Info about each course / workshop.
* Subscribe to courses and pay online.
* Members Area
* Photo gallery
* Contact us

The website will be implemented with our own made cms. We do not need it to be coded. We have a team ready to do this for us. We only need the PSD layout.

We have attached a mockup design that the client and I have come up with and we need the design to be taken to the next level.

Client also likes:
http://www.vellowindstudio.example/

Photographic Interests

Online

Requirements
Must have
• Must Stand out i.e black backgrounds
Should not have
• Alter the logo in anyway.

```html
<!DOCTYPE html>
<html lang="en">
<head>
<meta charset="utf-8">
<title>Your Lens Mate – Photographic Tuition</title>
<link rel="stylesheet" href="https://fonts.googleapis.com/css2?family=Bree+Serif&family=Oswald:wght@500&family=Open+Sans:ital,wght@0,400;0,600;0,700;1,400&family=Noto+Serif:wght@400;700&display=swap">
<style>
:root{
  --black:#141414;
  --header:#1d1d1d;
  --red:#e3262f;
  --orange:#d9792a;
  --green:#2fae4a;
  --purple:#b04aa2;
  --blue:#2f4fa0;
  --paper:#ffffff;
  --canvas:#e4e1dc;
  --ink:#222222;
  --accent-yellow:#9ccc1a;
  --link-blue:#2fa3d8;
  --footer:#1a1a1a;
}
*{box-sizing:border-box;margin:0;padding:0}
html,body{width:1200px;height:2545px;overflow:hidden}
body{font-family:"Open Sans",Arial,sans-serif;color:var(--ink);background:var(--canvas);position:relative}

/* Header */
.site-header{position:absolute;left:0;top:0;width:1200px;height:94px;background:linear-gradient(#2a2a2a,var(--header))}
.brand{position:absolute;left:145px;top:18px;display:flex;align-items:center;gap:12px}
.brand-dot{width:44px;height:44px;border-radius:50%;background:var(--red)}
.brand-name{font-family:"Noto Serif",Georgia,serif;font-weight:700;font-size:36px;color:#fff;line-height:1}
.brand-tag{position:absolute;left:201px;top:60px;font-size:14px;letter-spacing:4px;color:#fff}
.login{position:absolute;left:968px;top:28px;width:90px;height:32px;border:1px solid #555;border-radius:4px;background:linear-gradient(#3a3a3a,#1b1b1b);color:#fff;font-size:14px;font-weight:700;display:flex;align-items:center;justify-content:center;gap:8px}
.login i{width:10px;height:12px;border:2px solid #bbb;border-radius:2px}

.main-nav{position:absolute;left:0;top:94px;width:1200px;height:49px;background:var(--red);display:flex;justify-content:center;gap:40px;align-items:center}
.main-nav a{color:#fff;text-decoration:none;font-family:"Noto Serif",Georgia,serif;font-size:16px}

/* Hero */
.hero{position:absolute;left:0;top:143px;width:1200px;height:415px;background:linear-gradient(180deg,#9fc6e6 0%,#b9a58a 45%,#8a6a4a 62%,#2f6c8f 80%,#3d7fa0 100%)}
.hero-caption{position:absolute;left:140px;top:382px;width:590px}
.hero-title{background:var(--orange);color:#fff;font-family:"Oswald",sans-serif;font-size:27px;letter-spacing:1px;padding:6px 14px;display:inline-block;width:560px}
.hero-text{background:rgba(20,20,20,.72);color:#eee;font-style:italic;font-size:16px;line-height:24px;padding:12px 14px;width:590px}
.slider-bar{position:absolute;left:140px;top:536px;width:920px;height:60px;background:var(--black);clip-path:polygon(0 0,100% 0,98% 100%,2% 100%)}
.slider-arrow{position:absolute;top:16px;width:28px;height:28px;border:1px solid #555;border-radius:3px;display:flex;align-items:center;justify-content:center}
.dots{position:absolute;left:555px;top:26px;display:flex;gap:8px}
.dots span{width:9px;height:9px;border-radius:50%;background:#555}
.dots span:first-child{background:var(--red)}

/* Feature strip */
.feature-band{position:absolute;left:0;top:558px;width:1200px;height:336px;background:var(--paper)}
.features{position:absolute;left:140px;top:626px;width:920px;height:244px;background:#f1f1f1;border:1px solid #ddd;box-shadow:0 2px 5px rgba(0,0,0,.15);display:flex;gap:17px;padding:12px}
.feature{width:168px;position:relative}
.feature h3{font-family:"Noto Serif",Georgia,serif;font-weight:400;font-size:15px;line-height:17px;height:40px;display:flex;align-items:flex-end;padding-bottom:4px}
.feature .pic{height:90px;border:3px solid #fff;box-shadow:0 0 2px #999}
.feature p{font-size:11px;line-height:15px;margin-top:6px;color:#333}
.feature .bar{position:absolute;left:0;bottom:12px;width:168px;height:4px}

/* Content */
.column{position:absolute;left:140px;width:669px}
.section-head{height:34px;display:flex;justify-content:space-between;align-items:center;padding:0 12px;color:#fff;font-family:"Noto Serif",Georgia,serif;font-size:17px}
.section-head small{font-family:"Open Sans",sans-serif;font-size:13px;font-weight:600}
.post{position:relative;height:198px;background:var(--paper);border-bottom:5px solid #d5d2cd}
.date{position:absolute;left:-8px;top:24px;width:50px;height:50px;background:#9a9a9a;color:#fff;font-size:12px;font-weight:700;line-height:16px;text-align:center;padding-top:8px}
.post h2{position:absolute;left:60px;top:26px;font-family:"Bree Serif",serif;font-weight:400;font-size:21px}
.thumb{position:absolute;left:14px;top:84px;width:112px;height:105px;border:4px solid #fff;box-shadow:0 0 3px #888}
.post p{position:absolute;left:143px;top:68px;width:505px;font-size:13px;line-height:21px;color:#555}
.meta{position:absolute;left:143px;top:170px;font-size:11px;font-style:italic;color:#555;display:flex;gap:50px}

/* Sidebar */
.moon{position:absolute;left:853px;top:917px;width:206px;height:83px;border-radius:4px;background:linear-gradient(#1f3f9a,#0e1f55);display:flex;align-items:flex-end;justify-content:center;padding-bottom:12px;color:#fff;font-family:"Bree Serif",serif;font-size:19px}
.twilight{position:absolute;left:853px;top:1032px;width:206px;text-align:center;font-family:"Noto Serif",Georgia,serif;font-size:13px;line-height:17px;color:#333}
.calendar{position:absolute;left:853px;top:1075px;width:206px;height:228px;background:#3a3a3a;border-radius:3px;color:#fff}
.cal-head{height:30px;background:#262626;display:flex;justify-content:space-between;align-items:center;padding:0 10px;font-size:12px}
.cal-days,.cal-grid{display:grid;grid-template-columns:repeat(7,1fr);text-align:center}
.cal-days{font-size:8px;font-weight:700;height:16px;line-height:16px;background:#2e2e2e}
.cal-grid span{height:29px;line-height:29px;font-size:12px;font-weight:600}
.cal-grid .off{color:#777}
.cal-grid .on{background:#b3131b}
.widget-head{position:absolute;left:853px;width:206px;height:34px;color:#fff;font-size:14px;font-weight:600;padding:8px 12px}
.checklist{position:absolute;left:865px;top:1380px;list-style:none}
.checklist li{display:flex;align-items:center;gap:10px;font-size:12px;font-weight:700;height:32px}
.checklist i{width:20px;height:18px;border-radius:4px;background:var(--purple)}
.gallery{position:absolute;left:853px;top:1538px;display:grid;grid-template-columns:repeat(3,64px);gap:7px}
.gallery span{height:64px;border:3px solid #fff;box-shadow:0 0 2px #888}
.testimonial-label{position:absolute;left:855px;top:1906px;font-family:"Noto Serif",Georgia,serif;font-size:14px;font-weight:700}
.testimonial{position:absolute;left:853px;top:1932px;width:206px;height:216px;background:#fff;border:1px solid #ccc;padding:10px 12px;font-size:11px;font-style:italic;line-height:16px;color:#777;overflow:hidden}
.testimonial-tail{position:absolute;left:878px;top:2147px}
.testimonial-name{position:absolute;left:930px;top:2166px;font-size:12px;font-style:italic;color:var(--red)}

/* Footer */
.site-footer{position:absolute;left:0;top:2217px;width:1200px;height:328px;background:var(--footer);color:#ccc}
.f-contact{position:absolute;left:145px;top:40px;font-size:13px;line-height:20px}
.f-contact strong{color:#fff}
.phone{font-size:25px;font-weight:700;color:var(--accent-yellow);margin-top:6px;letter-spacing:1px}
.f-address{margin-top:24px;color:#aaa;font-size:12px;line-height:22px}
.f-address a{color:var(--link-blue)}
.f-courses{position:absolute;left:524px;top:40px;width:300px}
.f-courses h4{color:var(--link-blue);font-size:15px;font-weight:700;margin-bottom:14px}
.f-courses li{list-style:none;font-size:12px;color:#aaa;line-height:18px;margin-bottom:9px;padding-left:14px;position:relative}
.f-courses li::before{content:"";position:absolute;left:0;top:7px;width:4px;height:4px;background:#666}
.partners{position:absolute;left:905px;top:42px;display:flex;flex-direction:column;gap:16px}
.partners span{font-family:"Oswald",sans-serif;font-size:28px;line-height:34px;color:#3a3a3a}
.f-rule{position:absolute;left:140px;top:273px;width:920px;height:1px;background:#333}
.copyright{position:absolute;left:145px;top:291px;font-size:11px;color:#777}
.copyright em{color:var(--orange);font-style:normal}
.social{position:absolute;left:963px;top:286px;display:flex;gap:9px}
.social span{width:24px;height:24px;background:#444;border-radius:3px}
</style>
</head>
<body>

<header class="site-header">
  <div class="brand"><span class="brand-dot"></span><span class="brand-name">Your Lens Mate</span></div>
  <div class="brand-tag">PHOTOGRAPHIC TUITION</div>
  <div class="login">LOGIN <i></i></div>
</header>
<nav class="main-nav">
  <a>Home</a><a>About Us</a><a>Course / workshop</a><a>Subscribe &amp; Pay Online</a><a>Members Area</a><a>Photo Gallery</a><a>Contact Us</a>
</nav>

<section class="hero" role="img" aria-label="Photograph of an old European lakeside town with a covered wooden bridge and swans on the water"></section>
<div class="hero-caption">
  <div class="hero-title">NEQUE PORRO QUISQUAM ESTI DOLORE</div>
  <p class="hero-text">Lorem Ipsum is simply dummy text of the printing typesetting industry. Lorem Isdfpsum has been the industry. Lorem Ipsum is simply dummy text of the printing typesetting industry. Lorem Isdfpsum has been the industry's...</p>
</div>

<div class="feature-band"></div>
<div class="slider-bar">
  <div class="slider-arrow" style="left:56px"><svg width="10" height="12"><path d="M7 1L2 6l5 5" stroke="#ccc" stroke-width="2" fill="none"/></svg></div>
  <div class="dots"><span></span><span></span><span></span><span></span><span></span></div>
  <div class="slider-arrow" style="left:836px"><svg width="10" height="12"><path d="M3 1l5 5-5 5" stroke="#ccc" stroke-width="2" fill="none"/></svg></div>
</div>

<section class="features">
  <article class="feature"><h3 style="color:var(--blue)">Urban Excursion</h3><div class="pic" role="img" aria-label="Photo of a wooden boardwalk" style="background:linear-gradient(#8aa0b0,#6b5a4a)"></div><p>Lorem Ipsum is simply dummy text of the printing typesetting industry. Lorem Isdfpsum has been the industry's...</p><i class="bar" style="background:var(--blue)"></i></article>
  <article class="feature"><h3 style="color:var(--green)">Panorama</h3><div class="pic" role="img" aria-label="Panoramic photo of rooftops" style="background:linear-gradient(#c9d6e0,#8e6a55)"></div><p>Lorem Ipsum is simply dummy text of the printing typesetting industry. Lorem Isdfpsum has been the industry's...</p><i class="bar" style="background:var(--green)"></i></article>
  <article class="feature"><h3 style="color:var(--red)">Night Photography &amp; City Lights</h3><div class="pic" role="img" aria-label="Night photo of city light trails" style="background:linear-gradient(#2a2340,#c0603a)"></div><p>Lorem Ipsum is simply dummy text of the printing typesetting industry. Lorem Isdfpsum has been the industry's...</p><i class="bar" style="background:var(--red)"></i></article>
  <article class="feature"><h3 style="color:var(--purple)">City Walks</h3><div class="pic" role="img" aria-label="Photo of a city street" style="background:linear-gradient(#7a8aa0,#3a3a40)"></div><p>Lorem Ipsum is simply dummy text of the printing typesetting industry. Lorem Isdfpsum has been the industry's...</p><i class="bar" style="background:var(--purple)"></i></article>
  <article class="feature"><h3 style="color:var(--red)">HDR</h3><div class="pic" role="img" aria-label="HDR photo of a domed building with flowers" style="background:linear-gradient(#3a6fc0,#c44a4a)"></div><p>Lorem Ipsum is simply dummy text of the printing typesetting industry. Lorem Isdfpsum has been the industry's...</p><i class="bar" style="background:var(--orange)"></i></article>
</section>

<main>
  <section class="column" style="top:921px">
    <div class="section-head" style="background:var(--red)">General Information &amp; YLM's 2012<small>Read All »</small></div>
    <article class="post"><div class="date">JUN 10<br>2012</div><h2>Donec vulputate nulla in nibh pellentesque consequat.</h2><div class="thumb" role="img" aria-label="Photo of a tiger" style="background:linear-gradient(#c68a3c,#5a4028)"></div><p>Lorem ipsum dolor sit amet, consectetuer adipiscing elit. Donec semper risus id neque vulp elementum. Ut diam neque, vestibulum non, quis, commodo id, purus. Vivamus sagittis, odio non rhoncus adipiscing, elit ipsum pulvinar est, vitae malesuada velit orci sed arcu...</p><div class="meta"><span>◷ June 10, 2011</span><span>◯ No Comments</span></div></article>
    <article class="post"><div class="date">JUN 10<br>2012</div><h2>Donec vulputate nulla in nibh pellentesque consequat.</h2><div class="thumb" role="img" aria-label="Photo of a tiger" style="background:linear-gradient(#c68a3c,#5a4028)"></div><p>Lorem ipsum dolor sit amet, consectetuer adipiscing elit. Donec semper risus id neque vulp elementum. Ut diam neque, vestibulum non, quis, commodo id, purus. Vivamus sagittis, odio non rhoncus adipiscing, elit ipsum pulvinar est, vitae malesuada velit orci sed arcu...</p><div class="meta"><span>◷ June 10, 2011</span><span>◯ No Comments</span></div></article>
    <article class="post"><div class="date">JUN 10<br>2012</div><h2>Donec vulputate nulla in nibh pellentesque consequat.</h2><div class="thumb" role="img" aria-label="Photo of a tiger" style="background:linear-gradient(#c68a3c,#5a4028)"></div><p>Lorem ipsum dolor sit amet, consectetuer adipiscing elit. Donec semper risus id neque vulp elementum. Ut diam neque, vestibulum non, quis, commodo id, purus. Vivamus sagittis, odio non rhoncus adipiscing, elit ipsum pulvinar est, vitae malesuada velit orci sed arcu...</p><div class="meta"><span>◷ June 10, 2011</span><span>◯ No Comments</span></div></article>
  </section>

  <section class="column" style="top:1564px">
    <div class="section-head" style="background:var(--green)">USA Fall Travel Tour<small>Read All »</small></div>
    <article class="post"><div class="date">JUN 10<br>2012</div><h2>Donec vulputate nulla in nibh pellentesque consequat.</h2><div class="thumb" role="img" aria-label="Photo of green mountains" style="background:linear-gradient(#9cc0e0,#4f8a3a)"></div><p>Lorem ipsum dolor sit amet, consectetuer adipiscing elit. Donec semper risus id neque vulp elementum. Ut diam neque, vestibulum non, quis, commodo id, purus. Vivamus sagittis, odio non rhoncus adipiscing, elit ipsum pulvinar est, vitae malesuada velit orci sed arcu...</p><div class="meta"><span>◷ June 10, 2011</span><span>◯ No Comments</span></div></article>
    <article class="post"><div class="date">JUN 10<br>2012</div><h2>Donec vulputate nulla in nibh pellentesque consequat.</h2><div class="thumb" role="img" aria-label="Photo of green mountains" style="background:linear-gradient(#9cc0e0,#4f8a3a)"></div><p>Lorem ipsum dolor sit amet, consectetuer adipiscing elit. Donec semper risus id neque vulp elementum. Ut diam neque, vestibulum non, quis, commodo id, purus. Vivamus sagittis, odio non rhoncus adipiscing, elit ipsum pulvinar est, vitae malesuada velit orci sed arcu...</p><div class="meta"><span>◷ June 10, 2011</span><span>◯ No Comments</span></div></article>
    <article class="post"><div class="date">JUN 10<br>2012</div><h2>Donec vulputate nulla in nibh pellentesque consequat.</h2><div class="thumb" role="img" aria-label="Photo of green mountains" style="background:linear-gradient(#9cc0e0,#4f8a3a)"></div><p>Lorem ipsum dolor sit amet, consectetuer adipiscing elit. Donec semper risus id neque vulp elementum. Ut diam neque, vestibulum non, quis, commodo id, purus. Vivamus sagittis, odio non rhoncus adipiscing, elit ipsum pulvinar est, vitae malesuada velit orci sed arcu...</p><div class="meta"><span>◷ June 10, 2011</span><span>◯ No Comments</span></div></article>
  </section>
</main>

<aside>
  <div class="moon" role="img" aria-label="Night sky with moon illustration">Moon Phase Chart</div>
  <div class="twilight">Daily Shooting Times Nautical<br>Twilight Start to End</div>
  <div class="calendar">
    <div class="cal-head"><span>◂</span><span>July 2012</span><span>▸</span></div>
    <div class="cal-days"><span>MON</span><span>TUE</span><span>WED</span><span>THUR</span><span>FRI</span><span>SAT</span><span>SUN</span></div>
    <div class="cal-grid">
      <span class="off">26</span><span class="off">27</span><span class="off">28</span><span class="off">29</span><span class="off">30</span><span>1</span><span>2</span>
      <span>3</span><span>4</span><span>5</span><span>6</span><span>7</span><span>8</span><span>9</span>
      <span>10</span><span>11</span><span>12</span><span>13</span><span>14</span><span>15</span><span>16</span>
      <span>17</span><span>18</span><span>19</span><span>20</span><span>21</span><span class="on">22</span><span>23</span>
      <span>24</span><span>25</span><span>26</span><span>27</span><span>28</span><span>29</span><span>30</span>
      <span>31</span>
    </div>
  </div>
  <div class="widget-head" style="top:1334px;background:var(--purple)">Photograpers Check Lists</div>
  <ul class="checklist">
    <li><i></i>Wedding Shoot Check list</li>
    <li><i></i>Pre Shoot Check list</li>
    <li><i></i>Standard Check list</li>
  </ul>
  <div class="widget-head" style="top:1490px;background:var(--blue)">Members Gallery</div>
  <div class="gallery" role="img" aria-label="Grid of member photo thumbnails">
    <span style="background:#e8e4c8"></span><span style="background:#c2602e"></span><span style="background:#8a8a8a"></span>
    <span style="background:#e0a820"></span><span style="background:#2a3a8a"></span><span style="background:#3a4a6a"></span>
    <span style="background:#6a5a4a"></span><span style="background:#3a6ab0"></span><span style="background:#b01818"></span>
    <span style="background:#e8e4c8"></span><span style="background:#c2602e"></span><span style="background:#8a8a8a"></span>
    <span style="background:#e0a820"></span><span style="background:#2a3a8a"></span><span style="background:#3a4a6a"></span>
  </div>
  <div class="testimonial-label">Testimonials</div>
  <blockquote class="testimonial">Lorem ipsum dolor sit consectetuer adipiscing elit. Donec semper risus id neque vulp elementum. Ut diam neque, estium non, quis, commivamus sagittis, odio non rhoncus adipiscing, elit ipsum pulvinar est, vitae malesuada velit orci sed arcu. Lorem ipsum dolor sit consec-tetuer adipiscing elit. Donec semper risus id neque vulelt rhoncus adipiscing, elit ipsum.</blockquote>
  <svg class="testimonial-tail" width="26" height="22"><path d="M0 0h26L2 22z" fill="#fff"/><path d="M0 0L2 22 26 0" stroke="#ccc" fill="none"/></svg>
  <div class="testimonial-name">- Daniel Reed</div>
</aside>

<footer class="site-footer">
  <div class="f-contact">
    <strong>For more info about our courses,<br>please contact</strong>
    <div class="phone">0400 555 019</div>
    <div class="f-address">18 Harbour Lane, Unit 4,<br>MA 01234, Australia,<br>FAX: 0400 555 020<br><span style="color:#ddd">Email:</span> <a>hello@yourlensmate.example</a></div>
  </div>
  <div class="f-courses">
    <h4>OUR COURSES</h4>
    <ul>
      <li>Night Photography</li>
      <li>Learning the basics of Exposure, Aventure, ISO &amp; compresition</li>
      <li>Learning your camera funcations</li>
      <li>How to pick that good spot</li>
      <li>What equipment do I need</li>
    </ul>
  </div>
  <div class="partners"><span>Aperture Co</span><span>Filmworks</span><span>Lumen Optics</span><span>Brightline</span></div>
  <div class="f-rule"></div>
  <div class="copyright">Copyright © 2012 Your Lens Mate. All Rights Reserved. <em>Links &amp; Reviews</em></div>
  <div class="social"><span></span><span></span><span></span></div>
</footer>

</body>
</html>
```